Ovelin Watch app inspired by the Perch Thermostat

Wendle allows you to control your Perch Thermostat from your Ovelin Orbit device (Zentrix Watch).
The UI consists of two screens, phone and device, and the design will resemble the Perch look and feel (do not exactly copy, I need something that looks similar). The thermostat control will be front and center, with a white background and blue highlights.
A logo is also needed (custom typography is a plus).

My app is live in the Ovelin Bazaar Market at:
shop.zentrix.example/store/apps/details?id=com.brightforgeworks.wendle

The app currently supports the following devices:

The KV Qband:
https://shop.zentrix.example/store/devices/details?id=kv_q_band_black

The Tarvolo Rook Pulse:
https://shop.zentrix.example/store/devices/details?id=tarvolo_rook_pulse_black

Target Market(s)

Zentrix Watch wearers who have a Perch at home.

Industry/Entity Type

Ovelin

Colors
33a6d7
0555a3
3176b5
fefefe
85acd3
ffffff
cee9f5
cedeec
fbc994

Requirements
Must have
• Two screen designs:
• 1. A 1080 x 1920 px layout for ovelin phones.
• 2. A 320 x 320 px layout for Ovelin Orbit devices (please Zentrix "KV Q Band" or "Tarvolo Rook Pulse" for a visual of the devices I support).
• Design should resemble the Perch experience at perch.example. Using similar fonts, theme and shapes is a must. Please don't copy and paste elements. I need your interpretation of the UI, not the exact same elements from Perch.
• Please look at the screenshots of the Perch Ovelin app for inspiration:
• https://shop.zentrix.example/store/apps/details?id=com.perchworks.ovelin&hl=en
Nice to have
• The project consists of two rather simple layouts, so I'm asking for a logo for my app as well.
Should not have
• No black/dark backgrounds, no square buttons. Please approach the Perch look and feel as much as possible, especially in the QBand design.
• This should go without saying but:
• DO NOT copy paste elements from the Perch page. DO NOT plagiarize other peoples logos or artwork.
• Only original design work will win the contest.

```html
<!DOCTYPE html>
<html lang="en">
<head>
<meta charset="utf-8">
<title>Wendle – Watch Screens</title>
<link rel="stylesheet" href="https://fonts.googleapis.com/css2?family=Open+Sans:wght@300;400;600&display=swap">
<style>
  :root {
    --bg-start: #4a8fdc;
    --bg-mid: #8a86ef;
    --bg-end: #6aaaf0;
    --white: #ffffff;
    --screen-top: #fefefe;
    --screen-bottom: #eeeeee;
    --offline-ink: #5e5e5e;
    --offline-tick: #6a6a6a;
    --offline-scene-top: #9a9a9a;
    --offline-scene-bottom: #4a4a4a;
    --online-ink: #1e88e5;
    --online-tick: #3176b5;
    --online-mark: #0555a3;
    --online-scene-top: #ffcc00;
    --online-scene-bottom: #1da524;
    --symbol-grey: #bdbdbd;
  }
  * { margin: 0; padding: 0; box-sizing: border-box; }
  html, body { width: 1200px; height: 800px; overflow: hidden; }
  body {
    position: relative;
    font-family: "Open Sans", sans-serif;
    background: linear-gradient(135deg, var(--bg-start) 0%, var(--bg-mid) 55%, var(--bg-end) 100%);
    color: var(--white);
  }
  .brand {
    position: absolute;
    top: 52px;
    left: 0;
    width: 1200px;
    text-align: center;
    font-weight: 600;
    font-size: 78px;
    letter-spacing: 1px;
    color: var(--white);
  }
  .watch-screen {
    position: absolute;
    top: 289px;
    width: 356px;
    height: 356px;
  }
  .watch-screen--offline { left: 170px; }
  .watch-screen--online { left: 673px; }
  .watch-screen svg { display: block; width: 356px; height: 356px; }
  .temp-main { font-family: "Open Sans", sans-serif; font-weight: 400; font-size: 60px; }
  .temp-target { font-family: "Open Sans", sans-serif; font-weight: 400; font-size: 20px; }
  .room-label { font-family: "Open Sans", sans-serif; font-weight: 600; font-size: 20px; fill: var(--white); }
  .state-label {
    position: absolute;
    top: 722px;
    width: 356px;
    text-align: center;
    font-weight: 300;
    font-size: 44px;
    color: var(--white);
  }
  .state-label--offline { left: 170px; }
  .state-label--online { left: 673px; }
</style>
</head>
<body>

<div class="brand">Wendle</div>

<div class="watch-screen watch-screen--offline">
  <svg viewBox="0 0 320 320" xmlns="http://www.w3.org/2000/svg">
    <defs>
      <linearGradient id="screen-bg-off" x1="0" y1="0" x2="0" y2="1">
        <stop offset="0" stop-color="var(--screen-top)"/>
        <stop offset="1" stop-color="var(--screen-bottom)"/>
      </linearGradient>
      <linearGradient id="scene-off" x1="0" y1="0" x2="0" y2="1">
        <stop offset="0" stop-color="var(--offline-scene-top)"/>
        <stop offset="1" stop-color="var(--offline-scene-bottom)"/>
      </linearGradient>
    </defs>
    <rect width="320" height="320" fill="url(#screen-bg-off)"/>
    <path class="dial" d="M103.7 200.7 A91 91 0 1 1 218.3 200.7" fill="none"
          stroke="var(--offline-tick)" stroke-width="22" pathLength="282" stroke-dasharray="0.5 1.5"/>
    <g class="setpoint-marks" stroke="var(--offline-ink)" stroke-width="4">
      <line x1="242" y1="115" x2="266" y2="110"/>
      <line x1="243" y1="134" x2="267" y2="134"/>
    </g>
    <g class="adjust-icons" stroke="var(--symbol-grey)" stroke-width="1.6">
      <line x1="150" y1="80" x2="172" y2="80"/>
      <line x1="161" y1="69" x2="161" y2="91"/>
      <line x1="150" y1="191" x2="172" y2="191"/>
    </g>
    <text class="temp-main" x="161" y="157" text-anchor="middle" fill="var(--offline-ink)">78</text>
    <text class="temp-target" x="219" y="142" text-anchor="middle" fill="var(--offline-ink)">75</text>
    <rect class="scene" x="0" y="214" width="320" height="106" fill="url(#scene-off)"
          role="img" aria-label="Illustration: grey hillside at dusk with sun, trees and houses"/>
    <g class="status-icon" stroke="var(--white)" stroke-width="4" stroke-linecap="round">
      <line x1="151" y1="232" x2="171" y2="252"/>
      <line x1="171" y1="232" x2="151" y2="252"/>
    </g>
    <text class="room-label" x="160" y="302" text-anchor="middle">LIVING ROOM</text>
  </svg>
</div>

<div class="watch-screen watch-screen--online">
  <svg viewBox="0 0 320 320" xmlns="http://www.w3.org/2000/svg">
    <defs>
      <linearGradient id="screen-bg-on" x1="0" y1="0" x2="0" y2="1">
        <stop offset="0" stop-color="var(--screen-top)"/>
        <stop offset="1" stop-color="var(--screen-bottom)"/>
      </linearGradient>
      <linearGradient id="scene-on" x1="0" y1="0" x2="0" y2="1">
        <stop offset="0" stop-color="var(--online-scene-top)"/>
        <stop offset="1" stop-color="var(--online-scene-bottom)"/>
      </linearGradient>
    </defs>
    <rect width="320" height="320" fill="url(#screen-bg-on)"/>
    <path class="dial" d="M103.7 200.7 A91 91 0 1 1 218.3 200.7" fill="none"
          stroke="var(--online-tick)" stroke-width="22" pathLength="282" stroke-dasharray="0.5 1.5"/>
    <g class="setpoint-marks" stroke="var(--online-mark)" stroke-width="4">
      <line x1="242" y1="115" x2="266" y2="110"/>
      <line x1="243" y1="134" x2="267" y2="134"/>
    </g>
    <g class="adjust-icons" stroke="var(--symbol-grey)" stroke-width="1.6">
      <line x1="150" y1="80" x2="172" y2="80"/>
      <line x1="161" y1="69" x2="161" y2="91"/>
      <line x1="150" y1="191" x2="172" y2="191"/>
    </g>
    <text class="temp-main" x="161" y="157" text-anchor="middle" fill="var(--online-ink)">78</text>
    <text class="temp-target" x="219" y="142" text-anchor="middle" fill="var(--online-mark)">75</text>
    <rect class="scene" x="0" y="214" width="320" height="106" fill="url(#scene-on)"
          role="img" aria-label="Illustration: green hillside with yellow sun, trees and houses"/>
    <polyline class="status-icon" points="150,242 158,250 173,234" fill="none"
              stroke="var(--white)" stroke-width="4" stroke-linecap="round" stroke-linejoin="round"/>
    <text class="room-label" x="160" y="302" text-anchor="middle">LIVING ROOM</text>
  </svg>
</div>

<div class="state-label state-label--offline">Offline</div>
<div class="state-label state-label--online">Online</div>

</body>
</html>
```